Business card, Stationery and form for Crane Mill
Crane Mill, LLC an Energy Broker
Professional
Desmond Pilkerton
Principal
47 Birchway Lane
Fernbrook, OR 08539
(555) 214-KELP (5357)
dpilkerton@cranemill.com
www.cranemill.com
I will need to be able to change names etc on them for other workers.
Attached you will find a form that we use regularly (see the comment for the file).
I would also need the stationary designed in a way that is easy to use for word processing in MS Word, such as a template or in a word document that I can type on, besides in any way that may be printed.
I am guessing to use the secondary logo for the back but this is not required. An idea that I had but am unsure how it would look is to make that logo larger and then to place the words inside the lower grey area.
I may choose a full color design with pictures besides the more traditional one which I prefer in order to give the sales force a choice.
This is our primary logo
This is our secondary logo
This is a form which we use regularly. We primarily use the excel version here: http://cranemill.com/wp-content/uploads/2012/03/Crane-Mill-LOA-Form-unprotected.xlsx The form gets minor edits from time to time and I would prefer to have it designed as a header and footer or a template.

```html
<!DOCTYPE html>
<html lang="en">
<head>
<meta charset="utf-8">
<title>Crane Mill, LLC — Business Card</title>
<link href="https://fonts.googleapis.com/css2?family=Open+Sans:wght@400;600;700&family=Titillium+Web:wght@700;900&display=swap" rel="stylesheet">
<style>
  :root {
    --bg: #e9ebee;
    --card: #ffffff;
    --brand-blue: #1f4f9c;
    --brand-deep: #123a7a;
    --band-light: #3ec4e0;
    --band-dark: #1a5ea8;
    --ink: #3b3f45;
    --muted: #7c8591;
    --line: #1b1b1b;
    --tower-tone: #d9dde3;
  }
  * { box-sizing: border-box; margin: 0; padding: 0; }
  html, body { width: 1200px; height: 646px; overflow: hidden; }
  body {
    background: var(--bg);
    font-family: "Open Sans", Arial, sans-serif;
    color: var(--ink);
    position: relative;
  }
  .card {
    position: absolute;
    width: 540px;
    height: 309px;
    background: var(--card);
    box-shadow: 0 6px 18px rgba(0,0,0,.12);
    overflow: hidden;
  }
  .card--back { left: 40px; top: 168px; }
  .card--front { left: 620px; top: 168px; }

  /* back */
  .back-brand {
    position: absolute; left: 0; right: 0; top: 92px;
    display: flex; flex-direction: column; align-items: center;
  }
  .brand-mark {
    width: 70px; height: 70px; border-radius: 50%;
    background: var(--brand-blue);
    margin-bottom: 12px;
  }
  .brand-name {
    font-family: "Titillium Web", Arial, sans-serif;
    font-weight: 900;
    color: var(--brand-blue);
    letter-spacing: .5px;
    text-transform: uppercase;
    white-space: nowrap;
  }
  .back-brand .brand-name { font-size: 34px; line-height: 1; }
  .back-url {
    position: absolute; left: 0; right: 0; top: 222px;
    text-align: center; font-size: 12px; font-weight: 600;
    color: var(--brand-deep);
  }
  .back-band { position: absolute; left: 0; bottom: 0; width: 540px; height: 34px; }

  /* front */
  .front-band { position: absolute; left: 0; top: 0; width: 540px; height: 130px; }
  .holder {
    position: absolute; right: 26px; top: 20px; text-align: right; color: #fff;
  }
  .holder-name { font-size: 15px; font-weight: 700; }
  .holder-title { font-size: 11px; font-weight: 400; opacity: .9; }

  .tower-area {
    position: absolute; right: 10px; top: 118px; width: 210px; height: 160px;
    background: radial-gradient(ellipse at 55% 45%, var(--tower-tone), rgba(255,255,255,0) 70%);
  }

  .front-brand {
    position: absolute; left: 24px; top: 132px;
    display: flex; align-items: center; gap: 8px;
  }
  .front-brand .brand-mark { width: 34px; height: 34px; margin: 0; }
  .front-brand .brand-name { font-size: 30px; line-height: 1; }
  .tagline {
    position: absolute; left: 66px; top: 166px;
    font-size: 7px; font-weight: 700; letter-spacing: .8px;
    color: var(--brand-deep); text-transform: uppercase;
  }

  .contact {
    position: absolute; left: 66px; top: 186px;
    list-style: none; font-size: 9.5px; line-height: 15px; color: var(--ink);
  }
  .contact li { display: flex; align-items: center; gap: 7px; white-space: nowrap; }
  .contact .icon { width: 10px; height: 10px; flex: none; }
  .contact .addr { padding-left: 17px; }
</style>
</head>
<body>

  <section class="card card--back" aria-label="Business card back">
    <div class="back-brand">
      <span class="brand-mark"></span>
      <span class="brand-name">Crane Mill</span>
    </div>
    <p class="back-url">www.cranemill.com</p>
    <svg class="back-band" viewBox="0 0 540 34" aria-hidden="true">
      <defs>
        <linearGradient id="backBand" x1="0" x2="1">
          <stop offset="0" stop-color="#3ec4e0"/>
          <stop offset="1" stop-color="#1a5ea8"/>
        </linearGradient>
      </defs>
      <rect width="540" height="34" fill="url(#backBand)"/>
    </svg>
  </section>

  <section class="card card--front" aria-label="Business card front">
    <svg class="front-band" viewBox="0 0 540 130" aria-hidden="true">
      <defs>
        <linearGradient id="frontBand" x1="0" x2="1">
          <stop offset="0" stop-color="#3ec4e0"/>
          <stop offset=".55" stop-color="#2a8cc8"/>
          <stop offset="1" stop-color="#163f86"/>
        </linearGradient>
      </defs>
      <path d="M0 0 H540 V64 C420 50 330 70 250 96 C170 120 80 112 0 92 Z" fill="url(#frontBand)"/>
      <path d="M0 100 C90 124 180 128 262 104 C340 80 430 60 540 72" fill="none" stroke="#1b1b1b" stroke-width="4"/>
    </svg>

    <div class="holder">
      <p class="holder-name">Desmond Pilkerton</p>
      <p class="holder-title">Principal</p>
    </div>

    <div class="tower-area" role="img" aria-label="Line drawing of electricity transmission towers"></div>

    <div class="front-brand">
      <span class="brand-mark"></span>
      <span class="brand-name">Crane Mill, LLC</span>
    </div>
    <p class="tagline">Smart energy for your business</p>

    <ul class="contact">
      <li>
        <svg class="icon" viewBox="0 0 10 10" aria-hidden="true"><path d="M5 0.5a3 3 0 0 1 3 3c0 2.3-3 6-3 6s-3-3.7-3-6a3 3 0 0 1 3-3z" fill="#7c8591"/><circle cx="5" cy="3.5" r="1" fill="#fff"/></svg>
        47 Birchway Lane
      </li>
      <li class="addr">Fernbrook, OR 08539</li>
      <li>
        <svg class="icon" viewBox="0 0 10 10" aria-hidden="true"><path d="M2 0.8l1.6 2.2-0.9 1.1c.6 1.3 1.5 2.2 2.8 2.8l1.1-.9 2.2 1.6-.8 1.6C5 9 1 5 .4 1.6z" fill="#7c8591"/></svg>
        (555) 214-KELP (5357)
      </li>
      <li>
        <svg class="icon" viewBox="0 0 10 10" aria-hidden="true"><rect x="0.5" y="2" width="9" height="6.5" fill="#7c8591"/><path d="M0.5 2.2L5 5.6 9.5 2.2" fill="none" stroke="#fff" stroke-width=".8"/></svg>
        dpilkerton@cranemill.com
      </li>
      <li>
        <svg class="icon" viewBox="0 0 10 10" aria-hidden="true"><circle cx="5" cy="5" r="4.3" fill="none" stroke="#7c8591" stroke-width="1"/><path d="M0.7 5h8.6M5 0.7c-2.2 2.6-2.2 6 0 8.6M5 0.7c2.2 2.6 2.2 6 0 8.6" fill="none" stroke="#7c8591" stroke-width=".7"/></svg>
        www.cranemill.com
      </li>
    </ul>
  </section>

</body>
</html>
```